Email Template for AI Website Builder Marketing Campaign

Update: All the designs submitted have too much content for an email template. I have attached a mockup example of a simplified design. Please follow this guideline to revise your design to be less "wordy" and have less content to optimize the delivery rate of the emails. I have also attached the images I used to create the mockup. Feel free to use these images for your revised designs.
Original Brief:
I need a catchy email template for my new AI Website Builder, FolioNova.ai. The template must be professional, colorful, yet not too complex. The concept of the product is this:
FolioNova uses Artificial Intelligence (AI) to instantly build stunning websites, absolutely FREE. The user simply specifies their business name and business category (industry), and their stunning new website appears before their eyes!
The template will be used in MailChimp, so please provide the code that I can simply paste into the email body.
Here is a screenshot of our new website (which is not online yet) so you can match the color scheme and style of the email template to the new website design:
https://brindlemesh.com/mock_img/7720518/2638140/58190374/q8rt2lbw4k7ehnpyd3umc0xsvo_image.jpg
Let me know if you have any questions.
Thanks!
All submitted designs are too lengthy (too much content) for an email template. I will provide a mockup showing a sample of how you can simplify your design to function better as an email template and better suit my needs. I appreciate your patience!

```html
<!DOCTYPE html>
<html lang="en">
<head>
<meta charset="utf-8">
<title>FolioNova — Build website instantly</title>
<link href="https://fonts.googleapis.com/css2?family=Poppins:wght@400;500;600;700&display=swap" rel="stylesheet">
<style>
:root{
  --navy:#0c1660;
  --navy-deep:#0f0d4c;
  --ink:#17171f;
  --muted:#5c5f6b;
  --cyan:#36c9f1;
  --blue:#1a8ff0;
  --accent:#1ea4f0;
  --band:#dfe6fb;
  --line:#e4e6ec;
  --white:#ffffff;
}
*{margin:0;padding:0;box-sizing:border-box}
html,body{width:1200px;height:4354px;overflow:hidden;background:#fff;font-family:'Poppins',sans-serif}
.email{position:absolute;left:168px;top:125px;width:860px;box-shadow:0 10px 60px rgba(20,30,80,.12);background:#fff}
section,header,footer{position:relative;width:860px;overflow:hidden}
.abs{position:absolute}
.btn{position:absolute;display:flex;align-items:center;justify-content:center;background:linear-gradient(90deg,var(--cyan),var(--blue));color:#fff;font-weight:600;font-size:19px;text-transform:uppercase;border-radius:3px;letter-spacing:.2px}
.eyebrow{position:absolute;width:100%;text-align:center;color:var(--accent);font-weight:600;font-size:22px;line-height:30px}
.h2{position:absolute;width:100%;text-align:center;font-weight:600;font-size:37px;line-height:52px;color:var(--ink)}

/* hero */
.hero{height:801px;background:linear-gradient(160deg,#101a66 0%,#14237a 45%,#0d1a5c 100%)}
.hero .topbar{position:absolute;left:0;top:0;width:860px;height:137px;background:rgba(8,14,70,.55)}
.brand{position:absolute;display:flex;align-items:center;gap:12px;color:#fff;font-weight:500;font-size:35px;line-height:44px}
.brand .dot{width:26px;height:26px;border-radius:50%;background:var(--cyan)}
.nav a{position:absolute;top:53px;color:#fff;font-weight:600;font-size:20px;line-height:26px;text-decoration:none}
.hero-art{position:absolute;right:0;top:137px;width:500px;height:664px;background:radial-gradient(ellipse at 70% 50%,#3a7ee0 0%,#1c3d9a 35%,rgba(16,26,102,0) 70%)}
.hero h1{position:absolute;left:52px;top:238px;color:#fff;font-weight:700;font-size:47px;line-height:61px}
.hero p{position:absolute;left:52px;top:378px;width:520px;color:#e6ebff;font-size:23px;line-height:37px}
.wave{position:absolute;left:0;bottom:0}

/* why us */
.why{height:634px}
.why p.sub{position:absolute;width:100%;top:100px;text-align:center;color:var(--muted);font-size:20px;line-height:35px}
.card{position:absolute;top:211px;width:358px;height:338px;border:2px solid var(--line);border-radius:4px}
.card h3{position:absolute;left:42px;top:42px;font-weight:600;font-size:33px;line-height:49px;color:var(--ink)}
.card p{position:absolute;left:42px;top:154px;font-size:19px;line-height:35px;color:var(--muted)}
.card svg{position:absolute;right:14px;bottom:12px}

/* solutions */
.solutions{height:825px;background:radial-gradient(ellipse at 80% 90%,#1a2a7a 0%,rgba(18,15,79,0) 45%),radial-gradient(ellipse at 15% 20%,#1d2a72 0%,rgba(18,15,79,0) 40%),var(--navy-deep)}
.solutions .h2{color:#fff}
.feature{position:absolute;width:330px;color:#fff}
.feature svg{display:block}
.feature h4{position:absolute;left:0;font-weight:600;font-size:26px;line-height:34px}
.feature p{position:absolute;left:0;font-size:19px;line-height:29px;color:#dfe3f5;width:340px}

/* journey */
.journey{height:1117px}
.art{position:absolute;left:10px;top:245px;width:405px;height:305px;background:linear-gradient(135deg,#f3f5fa,#e7ecf7);border-radius:6px}
.journey h3{position:absolute;left:445px;top:318px;font-weight:600;font-size:30px;line-height:42px;color:var(--ink)}
.journey p.lead{position:absolute;left:445px;top:412px;font-size:23px;line-height:37px;color:var(--muted);width:380px}
.testi{position:absolute;top:914px}
.avatar{position:absolute;left:0;top:0;width:71px;height:71px;border-radius:50%}
.testi .quote{position:absolute;left:101px;top:0;width:260px;font-size:20px;line-height:36px;color:var(--muted)}
.testi .name{position:absolute;left:101px;top:84px;font-weight:600;font-size:28px;line-height:36px;color:var(--ink);white-space:nowrap}
.testi .role{position:absolute;left:101px;top:128px;font-size:20px;line-height:26px;color:var(--muted);white-space:nowrap}

/* cta */
.cta{height:284px;background:var(--band)}
.cta .kicker{position:absolute;left:57px;top:45px;color:var(--accent);font-weight:600;font-size:20px;line-height:28px}
.cta h2{position:absolute;left:57px;top:84px;font-weight:700;font-size:46px;line-height:61px;color:var(--ink)}
.cta .loop{position:absolute;left:0;top:0}

/* footer */
.footer{height:443px;background:linear-gradient(180deg,#0c1356 0%,#1a1352 100%);color:#fff}
.footer .about{position:absolute;left:57px;top:129px;font-size:20px;line-height:35px;width:240px}
.social{position:absolute;top:216px;width:41px;height:41px;border:2px solid #fff;border-radius:50%}
.col{position:absolute;top:64px}
.col h5{font-weight:600;font-size:23px;line-height:34px;margin-bottom:19px}
.col a{display:block;color:#fff;text-decoration:none;font-size:19px;line-height:34.5px}
.divider{position:absolute;left:57px;top:306px;width:746px;height:3px;background:#fff}
.legal{position:absolute;top:358px;font-size:20px;line-height:26px}
</style>
</head>
<body>
<div class="email">

  <header class="hero">
    <div class="topbar"></div>
    <div class="hero-art" role="img" aria-label="Glowing AI face formed from blue particles in space"></div>
    <div class="brand" style="left:52px;top:44px"><span class="dot"></span>FolioNova</div>
    <nav class="nav">
      <a style="left:429px">About</a>
      <a style="left:527px">Learn</a>
      <a style="left:620px">History</a>
      <a style="left:730px">Contact</a>
    </nav>
    <h1>Build website<br>instantly!</h1>
    <p>Let artificial intelligence build your stunning website instantly.</p>
    <a class="btn" style="left:52px;top:498px;width:385px;height:74px">Build your website</a>
    <svg class="wave" width="860" height="110" viewBox="0 0 860 110">
      <path d="M0 80 C 160 85 260 20 430 15 C 600 10 720 40 860 75 L860 110 L0 110 Z" fill="#fff"/>
      <path d="M0 80 C 160 85 260 20 430 15 C 600 10 720 40 860 75" fill="none" stroke="#1fb3f0" stroke-width="6"/>
    </svg>
  </header>

  <section class="why">
    <div class="h2" style="top:38px;font-size:40px">Why Us</div>
    <p class="sub">Lorem Ipsum is simply dummy text of the<br>printing and typesetting industry.</p>
    <div class="card" style="left:57px">
      <h3>Advancement<br>in AI</h3>
      <p>Lorem Ipsum is text simply<br>dummy Ipsum text.</p>
      <svg width="96" height="84" viewBox="0 0 96 84" fill="none" stroke="#1ea4f0" stroke-width="3">
        <circle cx="48" cy="42" r="36"/>
        <path d="M48 6 V78 M48 24 H66 M48 42 H72 M48 60 H66 M48 30 H30 M48 54 H30"/>
        <circle cx="70" cy="24" r="4"/><circle cx="76" cy="42" r="4"/><circle cx="70" cy="60" r="4"/>
      </svg>
    </div>
    <div class="card" style="left:445px">
      <h3>AI for website<br>Building</h3>
      <p>Lorem Ipsum is text simply<br>dummy Ipsum text.</p>
      <svg width="96" height="84" viewBox="0 0 96 84" fill="none" stroke="#1ea4f0" stroke-width="3">
        <rect x="4" y="6" width="88" height="58" rx="4"/>
        <path d="M38 64 V76 M58 64 V76 M28 78 H68"/>
        <path d="M16 20 H40 M16 32 H40 M16 44 H40 M54 18 H82 M54 28 H82 M54 38 H82 M54 48 H76"/>
      </svg>
    </div>
  </section>

  <section class="solutions">
    <div class="eyebrow" style="top:82px">Why FolioNova</div>
    <div class="h2" style="top:122px;color:#fff">We Provide Advanced Solutions<br>To Growin Your Business</div>

    <div class="feature" style="left:118px;top:313px">
      <svg width="74" height="70" viewBox="0 0 74 70" fill="none" stroke="#36c9f1" stroke-width="2.5">
        <circle cx="22" cy="35" r="14"/><circle cx="22" cy="35" r="6"/>
        <circle cx="52" cy="35" r="16"/><path d="M52 26 V44 M57 29 C52 25 46 29 52 34 C58 38 52 44 47 40"/>
      </svg>
      <h4 style="top:88px">Cost - Effective</h4>
      <p style="top:132px">AI eliminates the need for hiring expensive developers or agencies.</p>
    </div>
    <div class="feature" style="left:505px;top:313px">
      <svg width="74" height="70" viewBox="0 0 74 70" fill="none" stroke="#36c9f1" stroke-width="2.5">
        <rect x="4" y="2" width="40" height="66" rx="4"/>
        <path d="M12 16 H36 M12 28 H36 M12 40 H28"/>
        <circle cx="52" cy="14" r="10"/><circle cx="24" cy="56" r="5"/>
      </svg>
      <h4 style="top:88px">User - Friendly</h4>
      <p style="top:132px">User can easily navigate even without technical knowledge.</p>
    </div>
    <div class="feature" style="left:118px;top:555px">
      <svg width="74" height="74" viewBox="0 0 74 74" fill="none" stroke="#36c9f1" stroke-width="2.5">
        <rect x="2" y="2" width="70" height="70" stroke-dasharray="5 4"/>
        <rect x="24" y="24" width="26" height="26"/>
        <path d="M10 10 L22 22 M64 10 L52 22 M10 64 L22 52 M64 64 L52 52"/>
      </svg>
      <h4 style="top:92px">Scalability</h4>
      <p style="top:134px">It is easy to update or expand website using AI.</p>
    </div>
    <div class="feature" style="left:505px;top:555px">
      <svg width="74" height="74" viewBox="0 0 74 74" fill="none" stroke="#36c9f1" stroke-width="2.5">
        <circle cx="37" cy="37" r="33"/><circle cx="37" cy="37" r="24"/>
        <text x="37" y="45" text-anchor="middle" fill="#36c9f1" stroke="none" font-family="Poppins,sans-serif" font-size="22" font-weight="600">24</text>
      </svg>
      <h4 style="top:92px">27 / 7 Availability</h4>
      <p style="top:134px">You can build, update or manage at any time.</p>
    </div>
  </section>

  <section class="journey">
    <div class="eyebrow" style="top:47px">FolioNova</div>
    <div class="h2" style="top:87px">Begin your journey<br>with AI design</div>
    <div class="art" role="img" aria-label="Line illustration of a person working on a laptop with an AI thought bubble"></div>
    <h3>Grow up your<br>business with AI</h3>
    <p class="lead">Lorem Ipsum is simply dummy text of the printing.</p>
    <a class="btn" style="left:445px;top:529px;width:220px;height:74px">Read more</a>

    <div class="eyebrow" style="top:709px">Testimonials</div>
    <div class="h2" style="top:749px">What our site<br>Owners say</div>

    <div class="testi" style="left:57px">
      <div class="avatar" role="img" aria-label="Customer portrait" style="background:linear-gradient(135deg,#c9a08a,#6c7a88)"></div>
      <p class="quote">Lorem Ipsum is simply dummy text.</p>
      <p class="name">Maren Holloway</p>
      <p class="role">Small Business Owner</p>
    </div>
    <div class="testi" style="left:445px">
      <div class="avatar" role="img" aria-label="Customer portrait" style="background:linear-gradient(135deg,#d8322e,#3a2a24)"></div>
      <p class="quote">Lorem Ipsum is simply dummy text.</p>
      <p class="name">Tobin Reyes</p>
      <p class="role">Small Business Owner</p>
    </div>
  </section>

  <section class="cta">
    <svg class="loop" width="860" height="284" viewBox="0 0 860 284" fill="none" stroke="#ffffff" stroke-opacity=".55" stroke-width="3">
      <path d="M430 0 C 420 120 520 160 600 120 C 700 70 760 140 790 284"/>
      <path d="M620 0 C 660 60 740 70 860 40"/>
    </svg>
    <p class="kicker">Start building</p>
    <h2>Stop waiting<br>Try for free now!</h2>
    <a class="btn" style="left:559px;top:86px;width:244px;height:74px">Get in touch</a>
  </section>

  <footer class="footer">
    <div class="brand" style="left:57px;top:63px;font-size:33px"><span class="dot" style="width:24px;height:24px"></span>FolioNova</div>
    <p class="about">Lorem Ipsum is text simply dummy Ipsum</p>
    <span class="social" style="left:57px"></span>
    <span class="social" style="left:114px"></span>
    <span class="social" style="left:172px"></span>
    <span class="social" style="left:229px"></span>
    <div class="col" style="left:345px">
      <h5>Navigation</h5>
      <a>About FolioNova</a><a>Learn about AI</a><a>History of AI</a><a>Earn money</a>
    </div>
    <div class="col" style="left:617px">
      <h5>More Links</h5>
      <a>Contact Us</a><a>FAQ</a><a>Terms</a><a>Privacy</a>
    </div>
    <div class="divider"></div>
    <p class="legal" style="left:57px">@2023 FolioNova. All Rights Reserved.</p>
    <p class="legal" style="right:57px">Unsubscribe</p>
  </footer>

</div>
</body>
</html>
```